Online Marketing Agency Website

We are an online marketing agency that specializes in search marketing (SEM) for businesses of all sizes. Our core services include local search marketing, seo, paid search, paid social, graphic design, video production/editing and website design. We have an existing website that we launched a number of years ago but it's very outdated and we're currently too busy to design a new version.

Target Market(s)

Any business that needs online marketing services with an emphasis on search marketing.

Industry/Entity Type

Ad Agency

Number of Pages Required

4 page

Font styles to use
Sans Serif

Requirements
Must have
• Home page, interior page, blog page, contact us page.
Look and feel should be modern and clean and easy to navigate.
Sections for call outs for specific services: Business Marketing Strategy, Content Creation and Marketing, Graphic & Publication Design, Pay Per Click (PPC) Management, Search Engine Optimization, Social Media Management, Video Production & Editing, Website Hosting & Management, Website Design & Development
Use color from logo that was uploaded.

```html
<!DOCTYPE html>
<html lang="en">
<head>
<meta charset="utf-8">
<title>Ascend Digital — Online Marketing Elevated</title>
<link href="https://fonts.googleapis.com/css2?family=Poppins:wght@400;500;600;700&display=swap" rel="stylesheet">
<style>
:root{
  --orange:#f4511e;
  --ink:#2a2a2a;
  --text:#555;
  --soft:#f3f3f3;
  --blue:#3d7be0;
  --blue-light:#a9c9f5;
  --footer:#333333;
  --white:#ffffff;
}
*{box-sizing:border-box;margin:0;padding:0}
html,body{width:1200px;height:4573px;overflow:hidden}
body{position:relative;font-family:'Poppins',sans-serif;color:var(--ink);background:var(--white)}
.abs{position:absolute}
a{color:inherit;text-decoration:none}
.ph{position:absolute}

.hero-blob{position:absolute;left:0;top:0}
.brand{position:absolute;display:flex;align-items:center;gap:10px}
.brand-dot{width:22px;height:22px;border-radius:50%;background:var(--orange)}
.brand-name{font-weight:600;font-size:17px;line-height:1;letter-spacing:.3px;color:var(--ink)}
.brand-tag{font-size:10px;color:var(--ink);margin-top:3px}
.nav{position:absolute;left:518px;top:44px;display:flex;gap:38px;font-size:15px;font-weight:500}
.nav .active{color:var(--orange)}

.hero-title{left:89px;top:302px;font-size:44px;font-weight:600;line-height:46px;width:500px;letter-spacing:-.3px}
.hero-sub{left:89px;top:402px;font-size:25px;font-weight:600;color:var(--orange)}
.hero-text{left:89px;top:444px;font-size:14px;line-height:22px;width:400px;color:var(--text)}
.btn{position:absolute;display:flex;align-items:center;justify-content:center;border-radius:20px;font-weight:600;font-size:13px}
.btn-orange{background:var(--orange);color:var(--white)}

.section-title{position:absolute;left:0;width:1200px;text-align:center;font-size:42px;font-weight:600}
.intro{left:200px;width:800px;top:903px;text-align:center;font-size:15px;line-height:23px;color:var(--text)}

.service{position:absolute;width:330px}
.service-icon{width:128px;height:128px;border-radius:50%;background:linear-gradient(180deg,#ffffff,#ececec);display:flex;align-items:center;justify-content:center}
.service h3{font-size:19px;font-weight:600;margin-top:8px}
.service p{font-size:13px;line-height:21px;color:var(--text);margin-top:6px}
.btn-grey{background:#ebebeb;color:var(--ink)}

.about-title{left:667px;top:1818px;font-size:42px;font-weight:600}
.about-text{left:667px;top:1882px;width:440px;font-size:15px;line-height:24px;color:var(--text)}

.work-card{left:413px;top:2347px;width:375px;height:310px;background:var(--orange)}
.work-card h3{position:absolute;left:46px;top:170px;font-size:24px;line-height:26px;font-weight:600;color:var(--white)}
.work-card p{position:absolute;left:46px;top:236px;font-size:14px;line-height:18px;color:#ffe3d8;width:290px}
.work-btn{position:absolute;width:46px;height:46px;background:var(--white);display:flex;align-items:center;justify-content:center}

.blog-card{position:absolute;top:2858px;width:264px;height:399px;background:var(--white);box-shadow:0 6px 24px rgba(0,0,0,.08);border-radius:4px;overflow:hidden}
.blog-card .thumb{height:216px}
.blog-card h3{margin:30px 0 0 34px;font-size:19px;font-weight:600}
.blog-card p{margin:6px 30px 0 34px;font-size:12.5px;line-height:21px;color:var(--text)}
.blog-card .more{display:block;margin:12px 0 0 34px;font-size:13px;font-weight:600;color:var(--orange)}
.blog-feature{position:absolute;left:644px;top:2858px;width:467px;height:399px;border-radius:4px;overflow:hidden}
.blog-feature h3{position:absolute;left:48px;top:154px;font-size:30px;font-weight:600;color:var(--white)}
.blog-feature p{position:absolute;left:50px;top:202px;width:270px;font-size:13px;line-height:21px;color:#e8e8e8}

.love-title{left:89px;top:3508px;font-size:36px;line-height:40px;font-weight:600}
.love-title span{color:var(--orange)}
.love-text{left:89px;top:3602px;width:380px;font-size:15px;line-height:23px;color:var(--text)}
.arrow-btn{position:absolute;width:50px;height:50px;border-radius:50%;background:#efefef;display:flex;align-items:center;justify-content:center}
.quote-card{left:524px;top:3479px;width:372px;height:124px;background:var(--white);box-shadow:0 6px 24px rgba(0,0,0,.09);padding:20px 22px}
.quote-card h4{font-size:15px;font-weight:600}
.quote-card p{font-size:12px;line-height:18px;color:var(--text);margin-top:6px}
.stars{color:#f5a623;font-size:14px;letter-spacing:3px;margin-top:4px}
.avatar{position:absolute;border-radius:50%;border:5px solid var(--white);box-shadow:0 4px 14px rgba(0,0,0,.12)}

.newsletter{left:89px;top:3905px;width:1022px;height:222px;border-radius:111px;background:var(--orange)}
.newsletter h2{position:absolute;left:83px;top:62px;font-size:36px;line-height:36px;font-weight:700;color:var(--white)}
.newsletter p{position:absolute;left:80px;top:140px;font-size:17px;color:var(--white)}
.email{position:absolute;left:474px;top:85px;width:477px;height:52px;background:var(--white);border-radius:26px;font-size:16px;color:#555;padding:14px 28px}
.send{position:absolute;right:-1px;top:0;width:54px;height:52px;border-radius:50%;background:var(--footer);display:flex;align-items:center;justify-content:center}
.foot-col{position:absolute;top:4234px}
.foot-col h4{font-size:17px;font-weight:600;color:var(--white);margin-bottom:10px}
.foot-col li{list-style:none;font-size:13.5px;line-height:26.6px;color:#d6d6d6}
.contact li{display:flex;align-items:center;gap:8px}
.c-ico{width:11px;height:11px;border-radius:50%;background:var(--orange)}
.socials{display:flex;gap:10px;margin-top:10px}
.socials span{width:26px;height:26px;border-radius:50%;background:#555}
.rule{left:89px;top:4517px;width:1022px;height:1px;background:#4a4a4a}
.copyright{left:0;width:1200px;top:4536px;text-align:center;font-size:13px;font-weight:500;color:var(--white)}
</style>
</head>
<body>

<svg class="hero-blob" width="1200" height="780" viewBox="0 0 1200 780">
  <path d="M340 0 H1200 V690 C1120 780 960 790 840 740 C740 700 720 620 660 540 C600 460 520 360 530 260 C540 180 560 150 470 110 C380 70 345 40 340 0 Z" fill="var(--soft)"/>
</svg>

<header>
  <div class="brand" style="left:89px;top:50px">
    <span class="brand-dot"></span>
    <div><div class="brand-name">ASCEND DIGITAL</div><div class="brand-tag">Online Marketing. Elevated.</div></div>
  </div>
  <nav class="nav">
    <a class="active">Home</a><a>Our Services</a><a>Featured Work</a><a>Blog</a><a>About</a><a>Contact</a>
  </nav>
</header>

<section class="hero">
  <h1 class="abs hero-title">Ascend Digital<br>Online marketing</h1>
  <div class="abs hero-sub">Local SEO &amp; Business Listings</div>
  <p class="abs hero-text">85% of Consumers Use the Internet to Find Local Businesses. Are They Finding Yours?</p>
  <a class="btn btn-orange" style="left:89px;top:504px;width:158px;height:37px">GET STARTED</a>
  <div class="ph" role="img" aria-label="Illustration of a rocket launching beside a website screen with a team collaborating and a checklist" style="left:520px;top:120px;width:680px;height:480px;border-radius:50% 50% 46% 46%;background:radial-gradient(ellipse at 52% 48%,#5f97e8 0%,#8db6f0 28%,#c4d9f7 52%,#fbe1d6 72%,rgba(243,243,243,0) 86%)"></div>
</section>

<section class="services">
  <h2 class="section-title" style="top:845px">Our Services</h2>
  <p class="abs intro">Ascend Digital is a full-service online marketing agency.<br>We can handle any element of your online marketing so you can get back to doing what you do best — growing your business. All of our services are offered on an ‘a la carte’ basis.</p>

  <div class="service" style="left:87px;top:1026px">
    <div class="service-icon"><svg width="64" height="64" viewBox="0 0 64 64" fill="none" stroke-width="2.4" stroke-linecap="round"><path d="M10 10l10 10M20 10L10 20M44 44l10 10M54 44L44 54" stroke="var(--orange)"/><circle cx="50" cy="16" r="6" stroke="var(--orange)"/><path d="M44 18C24 22 40 40 22 44" stroke="var(--ink)" stroke-dasharray="3 4"/><circle cx="16" cy="48" r="6" stroke="var(--ink)"/></svg></div>
    <h3>Business Marketing Strategy</h3>
    <p>Let us strategize the big picture for you. With decades of experience, we have seen what works and what doesn’t. And we can leverage all that experience for your business.</p>
  </div>
  <div class="service" style="left:437px;top:1026px">
    <div class="service-icon"><svg width="64" height="64" viewBox="0 0 64 64" fill="none" stroke-width="2.4" stroke-linecap="round"><rect x="10" y="12" width="44" height="32" rx="2" stroke="var(--ink)"/><path d="M32 44v8M22 58l10-6 10 6" stroke="var(--ink)"/><rect x="22" y="18" width="20" height="22" stroke="var(--orange)"/><path d="M26 24h12M26 29h12M26 34h8" stroke="var(--orange)"/></svg></div>
    <h3>Content Creation and Marketing</h3>
    <p>You’ve heard it before. “Content is king.” Searchly loves it and potential customers expect it. Our content creators have years of experience working with major brands …</p>
  </div>
  <div class="service" style="left:788px;top:1026px">
    <div class="service-icon"><svg width="64" height="64" viewBox="0 0 64 64" fill="none" stroke-width="2.4" stroke-linecap="round"><rect x="16" y="8" width="34" height="44" stroke="var(--ink)"/><rect x="10" y="16" width="22" height="18" stroke="var(--orange)"/><path d="M12 32l7-8 5 5 4-4 4 5" stroke="var(--orange)"/><path d="M36 20h10M36 26h10M22 42h14" stroke="var(--ink)"/><circle cx="48" cy="50" r="6" stroke="var(--ink)"/></svg></div>
    <h3>Graphic &amp; Publication Design</h3>
    <p>Our designers have decades of experience in everything from tradeshow graphics to magazine layouts and logo design. If you need it, we can design it!</p>
  </div>
  <div class="service" style="left:87px;top:1290px">
    <div class="service-icon"><svg width="64" height="64" viewBox="0 0 64 64" fill="none" stroke-width="2.4" stroke-linecap="round"><circle cx="32" cy="36" r="12" stroke="var(--orange)"/><circle cx="32" cy="36" r="4" stroke="var(--orange)"/><path d="M32 8v8M26 16h12M14 54h36M20 54v-6M44 54v-6" stroke="var(--ink)"/><circle cx="12" cy="36" r="3" stroke="var(--ink)"/><circle cx="52" cy="36" r="3" stroke="var(--ink)"/></svg></div>
    <h3>Social Media Management</h3>
    <p>Scratching your head over how to make social media work for you? Our team has proven strategies that will help you win fans and solidify your brand as an expert voice.</p>
  </div>
  <div class="service" style="left:437px;top:1290px">
    <div class="service-icon"><svg width="64" height="64" viewBox="0 0 64 64" fill="none" stroke-width="2.4" stroke-linecap="round"><circle cx="14" cy="14" r="5" stroke="var(--orange)"/><circle cx="14" cy="30" r="5" stroke="var(--orange)"/><path d="M18 17l14 10M18 27l14-10" stroke="var(--orange)"/><rect x="32" y="10" width="22" height="40" stroke="var(--ink)"/><path d="M32 18h22M32 42h22M10 52h30" stroke="var(--ink)"/></svg></div>
    <h3>Video Production &amp; Editing</h3>
    <p>Video content is absolutely key in today’s SEO landscape. From scripting to publishing, we can help you create keyword rich, informative videos that both Searchly and clients! …</p>
  </div>
  <div class="service" style="left:788px;top:1290px">
    <div class="service-icon"><svg width="64" height="64" viewBox="0 0 64 64" fill="none" stroke-width="2.4" stroke-linecap="round"><rect x="8" y="10" width="40" height="32" stroke="var(--ink)"/><path d="M8 17h40M14 24h14M14 30h10" stroke="var(--ink)"/><circle cx="44" cy="44" r="12" stroke="var(--orange)" fill="#fff"/><path d="M32 44h24M44 32v24M36 37c5 3 11 3 16 0M36 51c5-3 11-3 16 0" stroke="var(--orange)"/></svg></div>
    <h3>Website Hosting &amp; Management</h3>
    <p>We will find you the most affordable, most-appropriate-for-your-business hosting solutions. What’s more, we’ll make sure your site stays online and be there for …</p>
  </div>
  <a class="btn btn-grey" style="left:488px;top:1587px;width:226px;height:39px;font-size:14px">VIEW MORE SERVICE</a>
</section>

<section class="about">
  <div class="ph" style="left:92px;top:1715px;width:508px;height:508px;border-radius:50%;background:linear-gradient(180deg,#f6f6f6,#ececec)"></div>
  <div class="ph" role="img" aria-label="Illustration of a team working together at a desk with charts and dashboards" style="left:110px;top:1830px;width:470px;height:310px;border-radius:40px;background:radial-gradient(ellipse at 45% 45%,#7fa9ea 0%,#b7cff3 35%,#f9cdb9 62%,rgba(236,236,236,0) 85%)"></div>
  <h2 class="abs about-title">About Us</h2>
  <p class="abs about-text">Lorem Ipsum is simply dummy text of the printing and typesetting industry. Lorem Ipsum has been the industry’s standard dummy text ever since the 1500s, when an unknown printer took a galley of type and scrambled it to make a type specimen book. It has survived not only five centuries, but also the leap into electronic typesetting, remaining essentially .</p>
  <a class="btn btn-orange" style="left:667px;top:2073px;width:148px;height:38px">READING MORE</a>
</section>

<section class="featured">
  <h2 class="section-title" style="top:2250px">Featured Work</h2>
  <div class="ph" role="img" aria-label="Photo of dark branded stationery with a red disc" style="left:0;top:2331px;width:400px;height:339px;background:linear-gradient(135deg,#2c2c2c,#3a3a3a 55%,#b3201d)"></div>
  <div class="ph" role="img" aria-label="Photo of branded stationery in orange" style="left:400px;top:2331px;width:402px;height:339px;background:#ee5a2a"></div>
  <div class="ph" role="img" aria-label="Photo of black business cards and a white disc" style="left:802px;top:2331px;width:398px;height:339px;background:linear-gradient(135deg,#1f1f1f,#2f2f2f 60%,#d9d9d9)"></div>
  <div class="abs work-card">
    <span class="work-btn" style="left:292px;top:32px"></span>
    <span class="work-btn" style="left:292px;top:88px">
      <svg width="18" height="18" viewBox="0 0 24 24" fill="none" stroke="#333" stroke-width="2.4" stroke-linecap="round"><path d="M10 14a4 4 0 0 0 5.7 0l3-3a4 4 0 0 0-5.7-5.7l-1 1"/><path d="M14 10a4 4 0 0 0-5.7 0l-3 3a4 4 0 0 0 5.7 5.7l1-1"/></svg>
    </span>
    <h3>Corporate Identity Development</h3>
    <p>Corporate Identity Development for Harper Lane Law</p>
  </div>
</section>

<section class="blog">
  <h2 class="section-title" style="top:2749px">Latest Blog</h2>
  <article class="blog-card" style="left:89px">
    <div class="thumb" role="img" aria-label="Photo of a hand holding a yellow paper plane" style="background:linear-gradient(160deg,#e6e6e6,#c9c9c9 55%,#e8d36a)"></div>
    <h3>Blog Heading</h3>
    <p>Lorem Ipsum is simply dummy text of the printing and typesetting industry.</p>
    <a class="more">READ MORE</a>
  </article>
  <article class="blog-card" style="left:366px">
    <div class="thumb" role="img" aria-label="Photo of a hand touching a digital marketing interface" style="background:linear-gradient(135deg,#0d2a4a,#2a6a9a)"></div>
    <h3>Blog Heading</h3>
    <p>Lorem Ipsum is simply dummy text of the printing and typesetting industry.</p>
    <a class="more">READ MORE</a>
  </article>
  <article class="blog-feature">
    <div class="ph" role="img" aria-label="Photo of a smartphone showing a social app in front of a laptop" style="inset:0;background:linear-gradient(90deg,#3d3d3d,#6b6b6b 60%,#9a9a9a)"></div>
    <h3>Blog Heading</h3>
    <p>Lorem Ipsum is simply dummy text of the printing and typesetting industry.</p>
    <a class="btn btn-orange" style="left:52px;top:248px;width:112px;height:32px;font-size:12px">READ MORE</a>
  </article>
</section>

<section class="testimonials">
  <h2 class="abs love-title">Which People Love<br><span>Ascend Digital</span></h2>
  <p class="abs love-text">Lorem ipsum dolor sit amet, consectetur adipisicing elit, sed do eiusmod tempor incididunt ut labore et dolore magna aliqua.</p>
  <span class="arrow-btn" style="left:92px;top:3692px"><svg width="10" height="12" viewBox="0 0 10 12"><path d="M7 1 2 6l5 5" fill="none" stroke="#333" stroke-width="2"/></svg></span>
  <span class="arrow-btn" style="left:149px;top:3692px"><svg width="10" height="12" viewBox="0 0 10 12"><path d="M3 1l5 5-5 5" fill="none" stroke="#333" stroke-width="2"/></svg></span>

  <div class="avatar" role="img" aria-label="Client portrait" style="left:661px;top:3431px;width:76px;height:76px;background:#5a6b78"></div>
  <div class="abs quote-card">
    <h4>John Doe</h4>
    <p>Lorem ipsum dolor sit am consectetur adipisicing elit, sed eiusmod tempor incididunt..</p>
    <div class="stars">★★★★★</div>
  </div>
  <div class="avatar" role="img" aria-label="Client portrait" style="left:811px;top:3362px;width:100px;height:100px;background:#9fd3e3"></div>
  <div class="avatar" role="img" aria-label="Client portrait" style="left:945px;top:3491px;width:108px;height:108px;background:#5fae4a"></div>
  <div class="avatar" role="img" aria-label="Client portrait" style="left:1084px;top:3620px;width:80px;height:80px;background:#c99a82"></div>
  <div class="avatar" role="img" aria-label="Client portrait" style="left:562px;top:3627px;width:108px;height:108px;background:#6b7a5c"></div>
  <div class="avatar" role="img" aria-label="Client portrait" style="left:803px;top:3620px;width:108px;height:108px;background:#f0a83a"></div>
  <div class="avatar" role="img" aria-label="Client portrait" style="left:691px;top:3755px;width:80px;height:80px;background:#d9d9d9"></div>
  <div class="avatar" role="img" aria-label="Client portrait" style="left:954px;top:3764px;width:62px;height:62px;background:#f2c7c0"></div>
</section>

<footer>
  <svg class="abs" style="left:0;top:4000px" width="1200" height="573" viewBox="0 0 1200 573">
    <path d="M0 60 C300 20 420 0 600 0 C780 0 900 20 1200 60 V573 H0 Z" fill="var(--footer)"/>
  </svg>
  <div class="abs newsletter">
    <h2>Subscribe to our<br>newsletter</h2>
    <p>Get notified of any updates!</p>
    <div class="email">Enter your email
      <span class="send"><svg width="18" height="18" viewBox="0 0 24 24"><path d="M2 11 22 3l-7 19-3-8z" fill="#fff"/></svg></span>
    </div>
  </div>

  <div class="brand" style="left:136px;top:4330px">
    <span class="brand-dot"></span>
    <div><div class="brand-name" style="color:#fff">ASCEND DIGITAL</div><div class="brand-tag" style="color:#ddd">Online Marketing. Elevated.</div></div>
  </div>

  <div class="foot-col" style="left:398px">
    <h4>Useful Links</h4>
    <ul><li>Home</li><li>Our Services</li><li>Featured Work</li><li>Blog</li><li>About</li><li>Contact</li></ul>
  </div>
  <div class="foot-col" style="left:579px">
    <h4>Services</h4>
    <ul><li>Business Marketing Strategy</li><li>Content Creation and Marketing</li><li>Graphic &amp; Publication Design</li><li>Pay Per Click (PPC) Management</li><li>Search Engine Optimization</li><li>Social Media Management</li></ul>
  </div>
  <div class="foot-col contact" style="left:859px">
    <h4>Contact Us</h4>
    <ul>
      <li><span class="c-ico"></span>Some goes address here</li>
      <li><span class="c-ico"></span>800-555-0142</li>
      <li><span class="c-ico"></span>800-555-0142</li>
      <li><span class="c-ico"></span>info@ascenddigital.com</li>
    </ul>
    <div class="socials"><span></span><span></span><span></span></div>
  </div>

  <div class="abs rule"></div>
  <p class="abs copyright">Copyright 2020 | All Rights Reserved</p>
</footer>

</body>
</html>
```